Home page design for a live auction website.

Hi, we are looking at finding a good design for an auction website, only home page .. We will not be selling anything online, so the website will only be a portal where visitors can check about our company, upcoming auctions, online catalogues etc.
See attached our logo. Please use the same red that you see on the logo in the designs that you provide.
The final design should communicate high-end auction website, as we will be selling expensive piece of arts and antiques.
We should have a main frame where images of arts will circulate, with description of the art piece. just like on http://paris.vellmarotte-quisande.com/
(but with a better design overall) and of course a menu with different tabs, like "about us", "previous sales" "next sales", "contact" , "how to buy", "meet our specialists".

Target Market(s)

High end segment, who can afford to pay up to 250'000 for a piece of art

Industry/Entity Type

Online

Number of Pages Required

1 page

Requirements
Must have
• a frame with images rotating, just like on http://paris.vellmarotte-quisande.com/ . but the rest of the design should be more refined.
• we should also have a strong call to action, "Free online estimation", click here, estimation delivered in 48 hours"
Nice to have
• Tremaux Auctions, the brand should be well visible

```html
<!DOCTYPE html>
<html lang="en">
<head>
<meta charset="utf-8">
<title>Tremaux Auctions</title>
<link href="https://fonts.googleapis.com/css2?family=Open+Sans:wght@400;600;700&family=Cinzel:wght@400;700&display=swap" rel="stylesheet">
<style>
:root{
  --red:#c4161c;
  --red-dark:#9e1015;
  --page:#eeeeee;
  --white:#ffffff;
  --ink:#333333;
  --muted:#777777;
  --line:#dddddd;
  --footer:#2f2f2f;
  --footer-bar:#1f1f1f;
  --gold:#b58a4a;
}
*{box-sizing:border-box;margin:0;padding:0}
html,body{width:831px;height:1200px;overflow:hidden}
body{font-family:"Open Sans",Arial,sans-serif;color:var(--ink);font-size:9px;
  background:linear-gradient(var(--red) 0,var(--red) 415px,var(--page) 415px);position:relative}
.site{position:absolute;left:42px;top:0;width:747px;height:1089px;background:var(--white)}
/* header */
.header{position:relative;height:96px;border-bottom:1px solid var(--line)}
.brand{position:absolute;left:16px;top:22px;display:flex;align-items:center;gap:8px}
.brand-square{width:26px;height:26px;background:var(--red)}
.brand-name{font-family:"Cinzel",Georgia,serif;font-weight:700;font-size:17px;color:var(--red);letter-spacing:.5px}
.search{position:absolute;right:120px;top:12px;width:120px;height:18px;border:1px solid var(--line);font-size:8px;color:#aaa;padding:3px 6px}
.search svg{position:absolute;right:4px;top:3px}
.social{position:absolute;right:14px;top:12px;display:flex;gap:4px}
.social span{width:18px;height:18px;border-radius:50%;background:#888}
.nav{position:absolute;right:14px;top:62px;display:flex}
.nav a{font-size:8.5px;font-weight:700;color:#444;text-decoration:none;padding:6px 10px;border-left:1px solid var(--line)}
.nav a:first-child{border-left:0}
.nav a.active{color:var(--white);background:var(--red)}
/* slider */
.slider{position:relative;height:330px;margin:4px 0 0}
.slide-art{position:absolute;inset:0;background:linear-gradient(135deg,#b8894a,#d9b57a 40%,#8a5a2c 75%,#5e3a1c)}
.arrow{position:absolute;top:150px;width:20px;height:30px;background:rgba(0,0,0,.55);display:flex;align-items:center;justify-content:center}
.arrow.prev{left:0}.arrow.next{right:0}
.caption{position:absolute;left:0;bottom:14px;width:470px;background:rgba(0,0,0,.72);color:var(--white);padding:9px 14px}
.caption h2{font-size:12px;font-weight:700;margin-bottom:4px}
.caption p{font-size:7.5px;line-height:1.45;color:#ddd}
.dots{position:absolute;right:14px;bottom:20px;display:flex;gap:4px}
.dots span{width:7px;height:7px;border-radius:50%;background:rgba(255,255,255,.6)}
.dots span.on{background:var(--red)}
/* welcome */
.welcome{text-align:center;padding:20px 50px 0}
.welcome h1{font-size:15px;font-weight:600;color:#444;margin-bottom:8px}
.welcome p{font-size:8px;line-height:1.6;color:var(--muted)}
/* columns */
.columns{display:flex;gap:14px;padding:26px 14px 0}
.col{flex:1;border:1px solid var(--line);height:360px}
.col-title{font-size:10px;font-weight:700;padding:8px 10px;border-bottom:1px solid var(--line);border-left:3px solid var(--red)}
.list-item{display:flex;gap:10px;padding:9px 10px;border-bottom:1px solid #eee}
.thumb{width:52px;height:52px;flex:none}
.item-date{font-size:7px;color:var(--muted);margin-bottom:3px}
.item-text{font-size:8.5px;font-weight:600;line-height:1.4}
.item-tag{font-size:7px;color:var(--red);margin-top:3px}
.cat .thumb{width:60px;height:80px}
.cat .list-item{padding:12px 10px 16px}
.video{padding:10px}
.video-thumb{position:relative;height:120px;margin-bottom:10px}
.play{position:absolute;left:50%;top:50%;width:30px;height:30px;margin:-15px 0 0 -15px;border-radius:50%;background:rgba(0,0,0,.55);display:flex;align-items:center;justify-content:center}
.view-all{display:flex;align-items:center;gap:6px;justify-content:center;font-size:9px;font-weight:700;margin-top:10px}
/* cta */
.cta{position:relative;margin:13px 14px 0;height:140px;display:flex;background:#f3ece2}
.cta-left{width:240px;background:linear-gradient(90deg,#6b4a2a,#a5753e 50%,#c6a276)}
.cta-box{width:240px;background:var(--red);color:var(--white);text-align:center;padding-top:18px}
.cta-box .free{font-family:"Cinzel",Georgia,serif;font-size:18px}
.cta-box .big{font-size:22px;font-weight:600;margin-top:2px}
.cta-btn{display:inline-block;margin:8px 0;background:var(--white);color:var(--red);font-weight:700;font-size:9px;padding:5px 14px}
.cta-box .note{font-size:8px}
.cta-right{flex:1;background:linear-gradient(90deg,#e9dcc6,#c9a77a 60%,#8c6a45)}
/* footer */
.footer{position:absolute;left:0;top:1089px;width:831px;height:89px;background:var(--footer);color:#ccc}
.footer-inner{position:absolute;left:55px;right:55px;top:22px;display:flex;gap:30px}
.contact{display:flex;gap:8px;width:150px}
.icon-circle{width:24px;height:24px;border-radius:50%;border:1px solid #777;display:flex;align-items:center;justify-content:center;flex:none}
.contact b{display:block;color:var(--white);font-size:8.5px;margin-bottom:2px}
.contact span{font-size:7.5px;line-height:1.4}
.alerts{margin-left:auto}
.alerts b{display:block;color:var(--white);font-size:8.5px;margin-bottom:5px}
.alerts .row{display:flex}
.alerts .field{width:120px;height:18px;background:var(--white)}
.alerts .btn{height:18px;background:var(--red);color:var(--white);font-weight:700;font-size:7.5px;padding:4px 8px}
.bottom{position:absolute;left:0;top:1178px;width:831px;height:22px;background:var(--footer-bar);color:#999;font-size:7.5px;display:flex;align-items:center;padding:0 55px;gap:14px}
.bottom .links{display:flex;gap:12px;margin-left:40px}
.bottom .social{position:static;margin-left:auto}
.bottom .social span{width:12px;height:12px;background:#666}
</style>
</head>
<body>
<div class="site">
  <header class="header">
    <div class="brand"><span class="brand-square"></span><span class="brand-name">Tremaux Auctions</span></div>
    <div class="search">Search
      <svg width="10" height="10" viewBox="0 0 10 10"><circle cx="4" cy="4" r="3" fill="none" stroke="#999" stroke-width="1.2"/><line x1="6.3" y1="6.3" x2="9" y2="9" stroke="#999" stroke-width="1.2"/></svg>
    </div>
    <div class="social"><span></span><span></span><span></span><span></span><span></span></div>
    <nav class="nav">
      <a href="#">ABOUT US</a><a href="#">PREVIOUS SALES</a><a href="#">NEXT SALES</a><a href="#">CONTACT</a><a href="#">HOW TO BUY</a><a href="#" class="active">MEET OUR SPECIALISTS</a>
    </nav>
  </header>

  <section class="slider">
    <div class="slide-art" role="img" aria-label="Featured artwork: ancient Egyptian painted panel with hieroglyphs"></div>
    <div class="arrow prev"><svg width="8" height="12"><path d="M7 1 2 6l5 5" fill="none" stroke="#fff" stroke-width="2"/></svg></div>
    <div class="arrow next"><svg width="8" height="12"><path d="M1 1l5 5-5 5" fill="none" stroke="#fff" stroke-width="2"/></svg></div>
    <div class="caption">
      <h2>Lorem ipsum dolor sit amet, consectetur adipiscing elit</h2>
      <p>Sed ut perspiciatis unde omnis iste natus error sit voluptatem accusantium doloremque laudantium, totam rem aperiam, eaque ipsa quae ab illo inventore veritatis.</p>
    </div>
    <div class="dots"><span class="on"></span><span></span><span></span><span></span></div>
  </section>

  <section class="welcome">
    <h1>Welcome to Tremaux Auctions</h1>
    <p>Lorem ipsum dolor sit amet, consectetur adipiscing elit, sed do eiusmod tempor incididunt ut labore et dolore magna aliqua. Ut enim ad minim veniam, quis nostrud exercitation ullamco laboris nisi ut aliquip ex ea commodo consequat. Duis aute irure dolor in reprehenderit in voluptate velit esse cillum dolore eu fugiat nulla pariatur. Excepteur sint occaecat cupidatat non proident, sunt in culpa qui officia deserunt mollit anim id est laborum.</p>
  </section>

  <section class="columns">
    <div class="col">
      <div class="col-title">Upcoming Auctions</div>
      <div class="list-item"><div class="thumb" style="background:#8c5a3a" role="img" aria-label="Auction lot: antique chair"></div><div><div class="item-date">20 Sep 2015</div><div class="item-text">Lorem ipsum dolor sit amet, consectetur adipiscing elit.</div></div></div>
      <div class="list-item"><div class="thumb" style="background:#b79a6a" role="img" aria-label="Auction lot: ornate cabinet"></div><div><div class="item-date">24 Sep 2015</div><div class="item-text">Lorem ipsum dolor sit amet, consectetur adipiscing elit.</div></div></div>
      <div class="list-item"><div class="thumb" style="background:#6e4f3a" role="img" aria-label="Auction lot: classical painting"></div><div><div class="item-date">02 Oct 2015</div><div class="item-text">Lorem ipsum dolor sit amet, consectetur adipiscing elit.</div></div></div>
      <div class="list-item"><div class="thumb" style="background:#a4302a" role="img" aria-label="Auction lot: red upholstered furniture"></div><div><div class="item-date">15 Oct 2015</div><div class="item-text">Lorem ipsum dolor sit amet, consectetur adipiscing elit.</div></div></div>
    </div>
    <div class="col cat">
      <div class="col-title">Online Catalogues</div>
      <div class="list-item"><div class="thumb" style="background:#c9a45a" role="img" aria-label="Catalogue cover: gilded figure"></div><div><div class="item-text">Lorem ipsum dolor sit amet, consectetur adipiscing elit.</div><div class="item-tag">Catalogue</div></div></div>
      <div class="list-item"><div class="thumb" style="background:#b08a5c" role="img" aria-label="Catalogue cover: bronze sculpture"></div><div><div class="item-text">Lorem ipsum dolor sit amet, consectetur adipiscing elit.</div><div class="item-tag">Catalogue</div></div></div>
      <div class="list-item"><div class="thumb" style="background:#2f5a9a" role="img" aria-label="Catalogue cover: painted Egyptian statue"></div><div><div class="item-text">Lorem ipsum dolor sit amet, consectetur adipiscing elit.</div><div class="item-tag">Catalogue</div></div></div>
    </div>
    <div class="col">
      <div class="col-title">Video</div>
      <div class="video">
        <div class="video-thumb" style="background:linear-gradient(135deg,#d9cbbb,#a3423a)" role="img" aria-label="Video preview: antique sofa in a salon">
          <div class="play"><svg width="10" height="12"><path d="M1 0v12l9-6z" fill="#fff"/></svg></div>
        </div>
        <div class="video-thumb" style="background:linear-gradient(135deg,#5a3a2a,#9a6a4a)" role="img" aria-label="Video preview: auction room furniture">
          <div class="play"><svg width="10" height="12"><path d="M1 0v12l9-6z" fill="#fff"/></svg></div>
        </div>
        <div class="view-all"><svg width="14" height="14"><rect width="14" height="14" rx="2" fill="#222"/><path d="M5 4v6l5-3z" fill="#fff"/></svg>View All Videos</div>
      </div>
    </div>
  </section>

  <section class="cta">
    <div class="cta-left" role="img" aria-label="Antique chest and porcelain vases"></div>
    <div class="cta-box">
      <div class="free">Free</div>
      <div class="big">Online Estimation</div>
      <div class="cta-btn">Click Here &rarr;</div>
      <div class="note">Estimation delivered in 48 hours</div>
    </div>
    <div class="cta-right" role="img" aria-label="Gilded antique armchair"></div>
  </section>
</div>

<footer class="footer">
  <div class="footer-inner">
    <div class="contact"><div class="icon-circle"><svg width="10" height="12"><path d="M5 0a4 4 0 0 0-4 4c0 3 4 8 4 8s4-5 4-8a4 4 0 0 0-4-4z" fill="#bbb"/><circle cx="5" cy="4" r="1.5" fill="#2f2f2f"/></svg></div><div><b>Contact</b><span>2020 Lorem ipsum dolor, sometis</span></div></div>
    <div class="contact"><div class="icon-circle"><svg width="12" height="9"><rect x=".5" y=".5" width="11" height="8" fill="none" stroke="#bbb"/><path d="M.5.5 6 5l5.5-4.5" fill="none" stroke="#bbb"/></svg></div><div><b>Email</b><span>info@tremauxauctions.com</span></div></div>
    <div class="contact"><div class="icon-circle"><svg width="10" height="10"><path d="M2 0l2 2-1 2 3 3 2-1 2 2-2 2C4 10 0 6 0 2z" fill="#bbb"/></svg></div><div><b>Phone</b><span>+888 123 456789</span></div></div>
    <div class="alerts"><b>AUCTION ALERTS!</b><div class="row"><div class="field"></div><div class="btn">SUBSCRIBE</div></div></div>
  </div>
</footer>
<div class="bottom">
  <span>&copy; Tremaux Auctions 2015</span>
  <div class="links"><span>About Us</span><span>Previous Sales</span><span>Next Sales</span><span>Contact</span><span>How To Buy</span><span>Meet Our Specialists</span></div>
  <div class="social"><span></span><span></span><span></span><span></span><span></span></div>
</div>
</body>
</html>
```